IT Services

We come to you
Only $49/hr
No contract, no monthly fee
Software engineer on staff
remote assistance or visit in your office

On the back of the card I want to list services.

- Server setup
- Network troubleshooting
- Printer setup
- Secure backup setup
- Software installation
- Wireless network setup
- Wired network setup
- Disaster recovery
- Website management
- Any other technology related support
- Email setup
- HIPAA compliance review and setup
Updates

the URL is: GEARFIXPRO.ZONE please use it on the card

On the card we need to mention "Connect remotely to address your IT issues" if there is enough room as well as "we go to you"

Industry/Entity Type

Printer

Contact Information for Business Card

I want a busoiness card to offer my services to doctor offices, it can be dentists, Otamatry, and other professions. I provide the following service. My plan is to go to their office and drop off my card. I don't want them to forget about it that is why I am paying for the design. I like hand writing design formats.

```html
<!DOCTYPE html>
<html lang="en">
<head>
<meta charset="utf-8">
<title>GearFixPro Zone – Business Card</title>
<link rel="stylesheet" href="https://fonts.googleapis.com/css2?family=Architects+Daughter&family=Open+Sans:wght@400;600;700&display=swap">
<style>
  :root {
    --page: #e9e7e4;
    --card: #ffffff;
    --orange: #f47a20;
    --peach: #fbc9a0;
    --navy: #142845;
    --grey: #7a7a7a;
    --ink: #2f2f2f;
    --hand: "Architects Daughter", cursive;
    --sans: "Open Sans", Arial, sans-serif;
  }
  * { box-sizing: border-box; margin: 0; padding: 0; }
  html, body { width: 1200px; height: 1000px; overflow: hidden; }
  body { background: var(--page); position: relative; font-family: var(--sans); }

  .card {
    position: absolute; left: 265px; width: 666px; height: 397px;
    background: var(--card);
    box-shadow: 0 3px 10px rgba(0,0,0,.18);
  }
  .card--front { top: 73px; }
  .card--back { top: 532px; }

  /* front */
  .brand-mark {
    position: absolute; left: 30px; top: 40px; width: 110px; height: 110px;
    border-radius: 50%; background: var(--orange);
  }
  .brand-url {
    position: absolute; left: 190px; top: 54px;
    font-family: var(--hand); font-size: 29px; letter-spacing: 1px;
    color: var(--grey);
  }
  .offer { position: absolute; left: 25px; top: 218px; }
  .offer__price { font-weight: 700; font-size: 16px; color: var(--grey); margin-bottom: 7px; }
  .offer__line { font-size: 16.5px; color: var(--orange); line-height: 25px; text-transform: uppercase; }

  .contact { position: absolute; right: 24px; top: 228px; text-align: right; }
  .contact__name { font-weight: 700; font-size: 26px; color: var(--navy); letter-spacing: .3px; }
  .contact__row { display: flex; justify-content: flex-end; align-items: center; gap: 4px; margin-top: 6px; }
  .contact__phone { font-weight: 700; font-size: 18px; color: var(--navy); }
  .contact__web { font-family: var(--hand); font-size: 14px; color: var(--grey); letter-spacing: .5px; }
  .contact__row svg { width: 16px; height: 16px; fill: var(--orange); }

  .band { position: absolute; top: 347px; height: 27px; background: var(--orange); }
  .band--left { left: 0; width: 398px; }
  .band--right { left: 403px; width: 263px; }

  /* back */
  .services { position: absolute; left: 32px; top: 64px; list-style: none; }
  .services li {
    display: flex; align-items: center; gap: 5px;
    font-size: 16px; line-height: 22.5px; color: var(--ink);
  }
  .services svg { width: 17px; height: 14px; fill: none; stroke: var(--orange); stroke-width: 2.4; stroke-linecap: round; stroke-linejoin: round; }

  .promo {
    position: absolute; left: 350px; top: 70px; width: 260px; height: 260px;
    display: flex; align-items: center; justify-content: center;
  }
  .promo__disc { position: absolute; inset: 0; border-radius: 50%; background: var(--peach); opacity: .45; }
  .promo__text { position: relative; font-weight: 700; font-size: 19px; color: var(--navy); }
</style>
</head>
<body>

<section class="card card--front">
  <div class="brand-mark"></div>
  <div class="brand-url">WWW.GEARFIXPRO.ZONE</div>

  <div class="offer">
    <p class="offer__price">ONLY $49/HR</p>
    <p class="offer__line">No contract, no monthly fee</p>
    <p class="offer__line">Software engineer on staff</p>
    <p class="offer__line">Remote assistance or visit in your office</p>
  </div>

  <div class="contact">
    <p class="contact__name">DAREN KOLBY</p>
    <div class="contact__row">
      <span class="contact__phone">1-800-555-0147</span>
      <svg viewBox="0 0 24 24" aria-hidden="true"><path d="M6.6 10.8a15.1 15.1 0 0 0 6.6 6.6l2.2-2.2c.3-.3.7-.4 1-.2 1.1.4 2.3.6 3.6.6.6 0 1 .4 1 1V20c0 .6-.4 1-1 1C10.6 21 3 13.4 3 4c0-.6.4-1 1-1h3.5c.6 0 1 .4 1 1 0 1.3.2 2.5.6 3.6.1.3 0 .7-.2 1z"/></svg>
    </div>
    <div class="contact__row">
      <span class="contact__web">WWW.GEARFIXPRO.ZONE</span>
      <svg viewBox="0 0 24 24" aria-hidden="true"><path d="M12 2a10 10 0 1 0 0 20 10 10 0 0 0 0-20zm6.9 6h-2.9a15.7 15.7 0 0 0-1.4-3.6A8 8 0 0 1 18.9 8zM12 4c.8 1.2 1.5 2.5 1.9 4h-3.8c.4-1.5 1.1-2.8 1.9-4zM4.3 14a8 8 0 0 1 0-4h3.4a16 16 0 0 0 0 4zm.8 2h2.9c.3 1.3.8 2.5 1.4 3.6A8 8 0 0 1 5.1 16zM8 8H5.1a8 8 0 0 1 4.3-3.6C8.8 5.5 8.3 6.7 8 8zm4 12c-.8-1.2-1.5-2.5-1.9-4h3.8c-.4 1.5-1.1 2.8-1.9 4zm2.3-6H9.7a14 14 0 0 1 0-4h4.6a14 14 0 0 1 0 4zm.3 5.6c.6-1.1 1.1-2.3 1.4-3.6h2.9a8 8 0 0 1-4.3 3.6zm1.7-5.6a16 16 0 0 0 0-4h3.4a8 8 0 0 1 0 4z"/></svg>
    </div>
  </div>

  <div class="band band--left"></div>
  <div class="band band--right"></div>
</section>

<section class="card card--back">
  <ul class="services">
    <li><svg viewBox="0 0 17 14"><path d="M2 8l4 4L15 2"/></svg>Server setup</li>
    <li><svg viewBox="0 0 17 14"><path d="M2 8l4 4L15 2"/></svg>Network troubleshooting</li>
    <li><svg viewBox="0 0 17 14"><path d="M2 8l4 4L15 2"/></svg>Printer setup</li>
    <li><svg viewBox="0 0 17 14"><path d="M2 8l4 4L15 2"/></svg>Secure backup setup</li>
    <li><svg viewBox="0 0 17 14"><path d="M2 8l4 4L15 2"/></svg>Software installation</li>
    <li><svg viewBox="0 0 17 14"><path d="M2 8l4 4L15 2"/></svg>Wireless network setup</li>
    <li><svg viewBox="0 0 17 14"><path d="M2 8l4 4L15 2"/></svg>Wired network setup</li>
    <li><svg viewBox="0 0 17 14"><path d="M2 8l4 4L15 2"/></svg>Disaster recovery</li>
    <li><svg viewBox="0 0 17 14"><path d="M2 8l4 4L15 2"/></svg>Website management</li>
    <li><svg viewBox="0 0 17 14"><path d="M2 8l4 4L15 2"/></svg>Any other technology related support</li>
    <li><svg viewBox="0 0 17 14"><path d="M2 8l4 4L15 2"/></svg>Email setup</li>
    <li><svg viewBox="0 0 17 14"><path d="M2 8l4 4L15 2"/></svg>HIPAA compliance review and setup</li>
  </ul>

  <div class="promo">
    <div class="promo__disc"></div>
    <p class="promo__text">WE COME TO YOU</p>
  </div>
</section>

</body>
</html>
```